Bright Arch Group business card

Bright Arch Group is the parent company of Bright Arch Building, Bright Arch Plumbing and Bright Arch Renovating. We require a sophisticated business card that covers all aspects of the building and plumbing space without using told or construction items.

Industry/Entity Type

Construction Company

Contact Information for Business Card

Gareth Pimley
Director
0472915083
gareth@brightarch.com.au
Www.brightarch.com.au

Font styles to use
Serif
Sans Serif

Colors
3176b5
ffce3e
0692cd
34a7d8
fbee3e
faa54b

Requirements
Must have
• Logo on front
• Logo and details on rear.
Nice to have
• Maybe water mark or shadow effect with logo
Should not have
• Tools or any construction associated items

```html
<!DOCTYPE html>
<html lang="en">
<head>
<meta charset="utf-8">
<title>Bright Arch Group – Business Card</title>
<link rel="stylesheet" href="https://fonts.googleapis.com/css2?family=Montserrat:wght@400;500;600&display=swap">
<style>
  :root {
    --stage: #2a2a2b;
    --card-dark: #050505;
    --card-light: #ffffff;
    --accent: #f5861f;
    --ink: #1b1b1b;
    --ink-soft: #333333;
  }
  * { box-sizing: border-box; margin: 0; padding: 0; }
  html, body { width: 1200px; height: 900px; overflow: hidden; }
  body {
    background: var(--stage);
    font-family: "Montserrat", Arial, sans-serif;
    position: relative;
  }
  .card {
    position: absolute;
    width: 620px;
    height: 355px;
    border-radius: 22px;
    overflow: hidden;
    box-shadow: 0 18px 40px rgba(0,0,0,.45);
  }

  /* Front */
  .card--front { left: 150px; top: 70px; background: var(--card-dark); }
  .front-mark {
    position: absolute; left: 0; right: 0; top: 120px;
    display: flex; align-items: center; justify-content: center; gap: 16px;
  }
  .front-mark__dot { width: 22px; height: 22px; border-radius: 50%; background: var(--accent); }
  .front-mark__name {
    color: var(--accent); font-weight: 500; font-size: 38px; letter-spacing: 6px;
  }
  .front-web {
    position: absolute; left: 300px; bottom: 40px;
    color: #fff; font-size: 14px; letter-spacing: .3px;
  }
  .front-web b { color: var(--accent); font-weight: 600; }
  .front-band {
    position: absolute; left: 0; bottom: 0; width: 64%; height: 22px; background: var(--accent);
  }
  .front-strip {
    position: absolute; right: 0; bottom: 0; width: 36%; height: 30px; background: var(--card-light);
  }

  /* Back */
  .card--back { left: 430px; top: 475px; background: var(--card-light); }
  .brand {
    position: absolute; left: 40px; top: 52px;
    display: flex; align-items: center; gap: 14px;
  }
  .brand__dot { width: 20px; height: 20px; border-radius: 50%; background: var(--accent); }
  .brand__name {
    color: var(--ink); font-weight: 400; font-size: 30px; letter-spacing: 7px; line-height: 1.15;
  }
  .person { position: absolute; right: 36px; top: 150px; text-align: right; }
  .person__name { color: var(--accent); font-weight: 600; font-size: 25px; }
  .person__role { color: var(--ink-soft); font-size: 13px; margin-top: 2px; }
  .divider {
    position: absolute; left: 36px; right: 36px; top: 218px; height: 1.5px; background: var(--ink);
  }
  .contacts { position: absolute; left: 40px; top: 236px; list-style: none; }
  .contacts li {
    display: flex; align-items: center; gap: 12px;
    color: var(--ink); font-size: 15px; height: 26px;
  }
  .contacts svg { width: 13px; height: 13px; fill: var(--accent); flex: none; }
  .contacts b { color: var(--accent); font-weight: 600; }
  .back-band {
    position: absolute; right: 0; bottom: 0; width: 36%; height: 22px; background: var(--accent);
  }
  .back-band-edge {
    position: absolute; right: 36%; bottom: 0; width: 34px; height: 22px; background: var(--card-dark);
  }
</style>
</head>
<body>

<section class="card card--front" aria-label="Card front">
  <div class="front-mark">
    <span class="front-mark__dot"></span>
    <span class="front-mark__name">BRIGHT ARCH</span>
  </div>
  <p class="front-web">www.<b>brightarch</b>.com.au</p>
  <div class="front-band"></div>
  <div class="front-strip"></div>
</section>

<section class="card card--back" aria-label="Card back">
  <div class="brand">
    <span class="brand__dot"></span>
    <span class="brand__name">BRIGHT ARCH<br>GROUP</span>
  </div>
  <div class="person">
    <p class="person__name">Gareth Pimley</p>
    <p class="person__role">Director</p>
  </div>
  <div class="divider"></div>
  <ul class="contacts">
    <li>
      <svg viewBox="0 0 24 24" aria-hidden="true"><path d="M6.6 10.8a15 15 0 0 0 6.6 6.6l2.2-2.2c.3-.3.7-.4 1-.2 1.1.4 2.3.6 3.6.6.6 0 1 .4 1 1V20c0 .6-.4 1-1 1A17 17 0 0 1 3 4c0-.6.4-1 1-1h3.5c.6 0 1 .4 1 1 0 1.3.2 2.5.6 3.6.1.3 0 .7-.2 1z"/></svg>
      0472915083
    </li>
    <li>
      <svg viewBox="0 0 24 24" aria-hidden="true"><path d="M2 5h20v14H2zM4 7v.5l8 5 8-5V7H4z"/></svg>
      gareth@brightarch.com.au
    </li>
    <li>
      <svg viewBox="0 0 24 24" aria-hidden="true"><path d="M12 2a10 10 0 1 0 0 20 10 10 0 0 0 0-20zm6.9 9h-3a15 15 0 0 0-1.2-5.6A8 8 0 0 1 18.9 11zM12 4.1c.9 1.2 1.7 3.8 1.9 6.9h-3.8c.2-3.1 1-5.7 1.9-6.9zM9.3 5.4A15 15 0 0 0 8.1 11h-3a8 8 0 0 1 4.2-5.6zM5.1 13h3a15 15 0 0 0 1.2 5.6A8 8 0 0 1 5.1 13zm6.9 6.9c-.9-1.2-1.7-3.8-1.9-6.9h3.8c-.2 3.1-1 5.7-1.9 6.9zm2.7-1.3a15 15 0 0 0 1.2-5.6h3a8 8 0 0 1-4.2 5.6z"/></svg>
      www.<b>brightarch</b>.com.au
    </li>
  </ul>
  <div class="back-band-edge"></div>
  <div class="back-band"></div>
</section>

</body>
</html>
```